Business Card Design - Law Firm

I need a business card design. I have attached a picture of the law firm's website and logo. The business card design should be consistent with those pictures. There should be a place for the employee name, employee job title, telephone number, facsimile number, address, website url, and email address for each employee.
Industry/Entity Type
Business

```html
<!DOCTYPE html>
<html lang="en">
<head>
<meta charset="utf-8">
<title>Whitcombe Law – Business Card</title>
<link rel="stylesheet" href="https://fonts.googleapis.com/css2?family=Cormorant+Garamond:wght@400;500&display=swap">
<style>
  :root {
    --backdrop: #3b3a39;
    --cream: #e3dbbd;
    --paper: #ffffff;
    --gold: #a38a4b;
    --gold-band: #a68a4a;
    --ink: #111111;
    --text-grey: #6f6f6f;
    --rule: #c9c9c9;
  }
  * { margin: 0; padding: 0; box-sizing: border-box; }
  html, body {
    width: 1200px; height: 1000px; overflow: hidden;
    background: var(--backdrop);
    font-family: "Cormorant Garamond", "Times New Roman", serif;
  }
  .canvas { position: relative; width: 1200px; height: 1000px; }

  .card {
    position: absolute; width: 762px; height: 466px;
    border-radius: 11px; overflow: hidden;
  }
  .card--front { left: 48px; top: 24px; background: var(--cream); }
  .card--back  { left: 385px; top: 504px; background: var(--paper); }

  .brand { position: absolute; display: flex; align-items: center; }
  .brand__square { background: var(--ink); flex: none; }
  .brand__name {
    color: var(--gold); font-weight: 500; line-height: 1; white-space: nowrap;
  }

  .card--front .brand { left: 0; right: 0; top: 170px; justify-content: center; gap: 22px; }
  .card--front .brand__square { width: 64px; height: 64px; }
  .card--front .brand__name { font-size: 52px; }

  .website {
    position: absolute; left: 0; right: 0; text-align: center;
    letter-spacing: 0.22em; font-weight: 500; line-height: 1;
  }
  .card--front .website { top: 440px; font-size: 29px; color: var(--gold); }

  .card--back .brand { left: 44px; top: 186px; gap: 18px; }
  .card--back .brand__square { width: 54px; height: 54px; }
  .card--back .brand__name { font-size: 37px; }

  .divider { position: absolute; width: 1px; background: var(--rule); }
  .divider--contact { left: 447px; top: 83px; height: 220px; }

  .contact { position: absolute; left: 463px; top: 0; color: var(--text-grey); }
  .contact__name {
    position: absolute; top: 80px; left: 0;
    font-size: 37px; color: var(--gold); font-weight: 400; line-height: 1;
  }
  .contact__title { position: absolute; top: 123px; left: 35px; font-size: 17px; color: #555; white-space: nowrap; }
  .contact__list { position: absolute; top: 174px; left: 0; list-style: none; font-size: 16.5px; line-height: 21px; white-space: nowrap; }
  .contact__list .indent { padding-left: 60px; }
  .contact__list .gap { margin-top: 9px; }

  .band {
    position: absolute; left: 0; right: 0; bottom: 0; height: 38px;
    background: var(--gold-band);
  }
  .band .website { top: 8px; font-size: 24px; color: var(--paper); }
</style>
</head>
<body>
<main class="canvas">
  <section class="card card--front" aria-label="Card front">
    <div class="brand">
      <span class="brand__square"></span>
      <span class="brand__name">Whitcombe Law</span>
    </div>
    <p class="website">www.website.com</p>
  </section>

  <section class="card card--back" aria-label="Card back">
    <div class="brand">
      <span class="brand__square"></span>
      <span class="brand__name">Whitcombe Law</span>
    </div>
    <span class="divider divider--contact"></span>
    <div class="contact">
      <h1 class="contact__name">Name</h1>
      <p class="contact__title">Job title</p>
      <ul class="contact__list">
        <li>address: 5345 Any Street west</li>
        <li class="indent">Townsvlle , ST&nbsp; 54321</li>
        <li class="gap">phone: 0400 318 662</li>
        <li>mobile: 0400 318 662</li>
        <li>fax: 0400 318 662</li>
        <li>email: email@mailbox.com.au</li>
      </ul>
    </div>
    <div class="band">
      <p class="website">www.website.com</p>
    </div>
  </section>
</main>
</body>
</html>
```